Illustrated restaurant promotional posters

We need series of 5 promotional posters for a restaurant, each one promoting a different special across the week. The text for each poster must be included and is in the file attached to this brief, but the design should only be treated as a draft idea for what we are looking for (we are flexible). We're looking to add illustrations to these posters, which may or may not require a complete re-imagining. The restaurant serves American BBQ with a latin twist, is smart casual, and the poster should reflect a welcoming, casual, but also elegant establishment. Images of food and the venue can be found here https://www.copperfernsmokehouse.com/

Target Market(s)

18 to 65, broad range of people, local restaurant, people popping in for a quick bite, and also celebrating main events

Industry/Entity Type

Restaurant

Font styles to use
Sans Serif

Colors
0054AA
0677BA
7BADD7
CADEEF
E8F1F8
EB3D1F
EC4F4E
F09395
F8D3D4
FCEDEE

Requirements
Must have
• Each poster must contain the text that is in the attached draft poster, illustration
Nice to have
• Colours similar to what is in attached file, though open to other otions

```html
<!DOCTYPE html>
<html lang="en">
<head>
<meta charset="UTF-8">
<title>Tuesday Special – Copperfern Smokehouse</title>
<link rel="stylesheet" href="https://fonts.googleapis.com/css2?family=Luckiest+Guy&family=Poppins:wght@700;800&display=block">
<style>
  :root {
    --paper: #e7e7e6;
    --ink: #161513;
    --brand-red: #e33a22;
    --cream: #f6e1c6;
    --shadow-soft: rgba(0, 0, 0, 0.10);
  }
  * { margin: 0; padding: 0; box-sizing: border-box; }
  html, body { width: 848px; height: 1200px; overflow: hidden; background: var(--paper); }
  .poster {
    position: relative;
    width: 848px;
    height: 1200px;
    background: var(--paper);
    color: var(--ink);
    overflow: hidden;
  }
  .brand {
    position: absolute;
    left: 52px;
    top: 92px;
    display: flex;
    align-items: center;
    gap: 8px;
  }
  .brand-dot {
    width: 14px;
    height: 14px;
    border-radius: 50%;
    background: var(--ink);
  }
  .brand-name {
    font-family: "Poppins", sans-serif;
    font-weight: 700;
    font-size: 14px;
    line-height: 1.15;
    letter-spacing: 1.5px;
    text-transform: uppercase;
    color: var(--ink);
  }
  .kicker {
    position: absolute;
    top: 155px;
    left: 0;
    width: 100%;
    text-align: center;
    font-family: "Poppins", sans-serif;
    font-weight: 800;
    font-size: 21px;
    line-height: 1;
    letter-spacing: 0.5px;
    color: var(--ink);
  }
  .display {
    position: absolute;
    left: 0;
    width: 100%;
    text-align: center;
    font-family: "Luckiest Guy", "Arial Black", Impact, sans-serif;
    font-weight: 900;
    text-transform: uppercase;
    line-height: 1;
    white-space: nowrap;
  }
  .headline-day {
    top: 204px;
    font-size: 90px;
    color: var(--ink);
    letter-spacing: 1px;
  }
  .headline-offer {
    top: 292px;
    font-size: 132px;
    color: var(--brand-red);
    letter-spacing: 1px;
    text-shadow: 4px 5px 0 var(--shadow-soft);
  }
  .mascot {
    position: absolute;
    left: 128px;
    top: 466px;
    width: 592px;
    height: 400px;
    border-radius: 28px;
    background: linear-gradient(180deg, var(--cream) 0%, #f1d3b6 55%, #e8836e 100%);
  }
  .price {
    top: 930px;
    font-size: 88px;
    color: var(--ink);
  }
  .price-unit {
    top: 1034px;
    font-size: 100px;
    color: var(--brand-red);
    letter-spacing: 2px;
  }
</style>
</head>
<body>
  <main class="poster">
    <header class="brand">
      <span class="brand-dot"></span>
      <span class="brand-name">Copperfern<br>Smokehouse</span>
    </header>

    <p class="kicker">Special Present</p>
    <h1 class="display headline-day">Tuesday</h1>
    <h2 class="display headline-offer">Special</h2>

    <div class="mascot" role="img" aria-label="Cartoon serving cloche mascot with arms and red shoes, walking and giving a thumbs up, surrounded by red sparkles"></div>

    <p class="display price">$25</p>
    <p class="display price-unit">Per Person</p>
  </main>
</body>
</html>
```